KR TMW PowerPoint Template Design

Looking for an eye catching and clean powerpoint template to deliver sales proposals to our clients. KR TMW is a sales and marketing representation business in the hospitality industry, Logo it attached.

```html
<!DOCTYPE html>
<html lang="en">
<head>
<meta charset="utf-8">
<title>KR TMW Presentation Template</title>
<link href="https://fonts.googleapis.com/css2?family=Montserrat:wght@400;600;700;800&family=Open+Sans:wght@400;600;700&display=swap" rel="stylesheet">
<style>
:root{
  --gold:#9b875a;
  --gold-dark:#7a6a43;
  --gold-light:#c9b88f;
  --gold-pale:#e9e1cf;
  --ink:#262626;
  --grey:#7c7c7c;
  --grey-light:#cfcfcf;
  --orange:#c5601c;
  --mustard:#c9a12a;
  --olive:#6f6440;
  --green:#4c9a3a;
  --paper:#ffffff;
  --canvas:#ffffff;
}
*{box-sizing:border-box;margin:0;padding:0}
html,body{width:1200px;height:2507px;overflow:hidden;background:var(--canvas)}
body{font-family:"Open Sans",Arial,sans-serif;color:var(--ink)}
.deck{display:grid;grid-template-columns:repeat(3,386px);grid-auto-rows:217px;column-gap:11px;row-gap:10px;padding:10px}
.deck-end{grid-column:1 / 4;display:flex;justify-content:center;gap:11px}
.slide{position:relative;width:386px;height:217px;overflow:hidden;background:var(--paper);box-shadow:0 0 0 1px #eee}
.ph{position:absolute}
.abs{position:absolute}
.h{font-family:"Montserrat",Arial,sans-serif;font-weight:700}
.slide-title{position:absolute;left:16px;top:14px;font-family:"Montserrat",Arial,sans-serif;font-weight:700;font-size:12px;color:var(--ink)}
.brand-mini{position:absolute;right:10px;top:8px;font-family:"Montserrat",Arial,sans-serif;font-weight:700;font-size:7px;color:var(--gold);letter-spacing:.5px}
.foot{position:absolute;left:16px;right:40px;bottom:12px;height:1px;background:var(--gold)}
.pg{position:absolute;right:14px;bottom:8px;font-size:5px;color:var(--grey);border:1px solid var(--gold-light);padding:1px 3px}
.tiny{font-size:5px;line-height:1.45;color:var(--grey)}
.tiny b{color:var(--ink);font-weight:700}
.small{font-size:6px;line-height:1.45;color:var(--ink)}
.wt{color:#fff}
.gold{color:var(--gold)}
</style>
</head>
<body>
<main class="deck">

<!-- 1 cover -->
<section class="slide">
  <div class="ph" role="img" aria-label="Photo of glass skyscrapers seen from below" style="inset:0;background:linear-gradient(135deg,#3b4048 0%,#9aa3ad 40%,#dfe3e6 60%,#5c6169 100%)"></div>
  <div class="abs" style="left:90px;top:20px;width:206px;height:140px;background:rgba(255,255,255,.88)"></div>
  <div class="abs h" style="left:90px;top:66px;width:206px;text-align:center;font-size:26px;color:var(--gold)">KR TMW</div>
  <div class="abs tiny" style="left:90px;top:100px;width:206px;text-align:center">SALES &amp; MARKETING REPRESENTATION</div>
  <div class="abs" style="left:0;top:170px;width:386px;height:28px;background:rgba(255,255,255,.9)"></div>
  <div class="abs h" style="left:60px;top:179px;font-size:9px;color:var(--gold)">WRITE YOUR PRESENTATION NAME</div>
</section>

<!-- 2 -->
<section class="slide">
  <div class="ph" role="img" aria-label="Photo of a business meeting around a table" style="inset:0;background:linear-gradient(100deg,#c9c4bb 0%,#8d8375 35%,#e4e0da 55%,#6d6358 100%)"></div>
  <div class="abs" style="left:110px;top:30px;width:166px;height:150px;border:2px solid #fff;background:rgba(255,255,255,.25)"></div>
  <div class="abs h" style="left:110px;top:90px;width:166px;text-align:center;font-size:24px;color:var(--gold-dark)">KR TMW</div>
</section>

<!-- 3 -->
<section class="slide">
  <div class="ph" role="img" aria-label="Faded photo of a city skyline" style="inset:0;background:linear-gradient(180deg,#f2f2f2 0%,#d4d6d8 55%,#a9adb1 100%)"></div>
  <svg class="abs" style="left:0;top:0" width="386" height="217"><polygon points="250,0 300,0 386,55 386,85" fill="#9b875a"/><polygon points="320,0 386,0 386,30" fill="#c9b88f"/><polygon points="0,217 30,217 0,200" fill="#9b875a"/></svg>
  <div class="abs h" style="left:40px;top:85px;font-size:18px;line-height:1.15;color:var(--ink);font-weight:600">Click to edit<br>Master title style</div>
  <div class="abs h" style="right:14px;bottom:12px;font-size:10px;color:var(--gold)">KR TMW</div>
</section>

<!-- 4 -->
<section class="slide">
  <div class="ph" role="img" aria-label="Photo of a man in a suit writing at a desk" style="inset:0;background:linear-gradient(90deg,#a18d61 0%,#c1ae85 35%,#d8d2c6 60%,#8f8576 100%)"></div>
  <div class="abs h wt" style="left:22px;top:92px;font-size:34px;font-weight:800">PROPOSAL</div>
  <div class="abs tiny wt" style="left:22px;top:136px;width:200px;color:#fff">Lorem ipsum dolor sit amet, consectetur adipiscing elit, sed do eiusmod tempor incididunt ut labore et dolore magna.</div>
</section>

<!-- 5 -->
<section class="slide">
  <div class="ph" role="img" aria-label="Photo of tall office towers at sunset" style="left:0;top:0;width:150px;height:217px;background:linear-gradient(180deg,#6f8c8f 0%,#a9b3aa 40%,#c77c3c 75%,#4f4a42 100%)"></div>
  <div class="abs h wt" style="left:16px;top:40px;font-size:34px;font-weight:800">90%</div>
  <div class="abs tiny" style="left:16px;top:82px;width:120px;color:#fff">Lorem ipsum dolor sit amet, consectetur adipiscing elit sed do.</div>
  <div class="brand-mini">KR TMW</div>
  <div class="abs h" style="left:180px;top:80px;font-size:9px;font-weight:600">Lorem ipsum dolor sit amet</div>
  <div class="abs h" style="left:190px;top:94px;font-size:15px">adipiscing elit</div>
  <div class="abs h" style="left:204px;top:113px;font-size:15px;color:var(--gold)">Consectetur</div>
  <div class="abs" style="left:16px;right:40px;bottom:12px;height:1px;background:var(--gold)"></div>
  <div class="pg">05</div>
</section>

<!-- 6 -->
<section class="slide">
  <div class="ph" role="img" aria-label="Photo of a woman with glasses working, gold tinted" style="inset:0;background:linear-gradient(120deg,#8a7a55 0%,#b9a67e 45%,#d6cbb2 60%,#8b7b56 100%)"></div>
  <div class="abs h wt" style="left:60px;top:22px;width:266px;text-align:center;font-size:17px;line-height:1.2">LOREM IPSUM DOLOR SIT AMET</div>
  <svg class="abs" style="left:104px;top:108px" width="16" height="20"><circle cx="8" cy="7" r="6" fill="none" stroke="#fff" stroke-width="1.4"/><rect x="5" y="14" width="6" height="4" fill="#fff"/></svg>
  <svg class="abs" style="left:258px;top:108px" width="18" height="18"><polygon points="9,1 11.5,7 18,7 13,11 15,17 9,13.5 3,17 5,11 0,7 6.5,7" fill="#fff"/></svg>
  <div class="abs tiny" style="left:60px;top:148px;width:110px;height:22px;line-height:22px;text-align:center;background:rgba(122,106,67,.85);color:#fff;font-size:6px">Innovative Strategies</div>
  <div class="abs tiny" style="left:212px;top:148px;width:120px;height:22px;line-height:22px;text-align:center;background:rgba(122,106,67,.85);color:#fff;font-size:6px">Our Commitment to our Clients</div>
</section>

<!-- 7 -->
<section class="slide">
  <div class="ph" role="img" aria-label="Photo of a businessman at a desk with a laptop" style="inset:0;background:linear-gradient(90deg,#b29e72 0%,#d3c6a6 40%,#8d857a 70%,#c8c1b4 100%)"></div>
  <div class="abs" style="left:0;top:30px;width:210px;height:170px;background:rgba(201,184,143,.75)"></div>
  <div class="abs h" style="left:12px;top:36px;font-size:17px;line-height:1.12;font-weight:800;color:var(--ink)">IMAGINATION<br>MEANS<br>NOTHING<br>WITHOUT<br><span class="wt">DOING</span></div>
  <div class="abs tiny" style="left:122px;top:162px;width:120px;color:#fff">Lorem ipsum dolor sit amet, consectetur adipiscing elit sed do eiusmod.</div>
  <div class="pg">07</div>
</section>

<!-- 8 -->
<section class="slide">
  <div class="ph" role="img" aria-label="Top view photo of a desk with keyboard, glasses and coffee" style="left:0;top:0;width:175px;height:217px;background:linear-gradient(160deg,#f4f4f4 0%,#e6e6e6 50%,#cfcfcf 100%)"></div>
  <div class="brand-mini">KR TMW</div>
  <div class="abs h" style="left:200px;top:16px;font-size:9px;font-weight:600">Lorem ipsum dolor sit amet</div>
  <div class="abs h" style="left:192px;top:90px;font-size:14px">UP TO</div>
  <div class="abs h" style="left:205px;top:96px;font-size:50px;font-weight:800;color:var(--gold)">100</div>
  <div class="abs h" style="left:268px;top:157px;font-size:6px">EVERY MONTH</div>
  <div class="abs" style="left:190px;right:40px;bottom:12px;height:1px;background:var(--gold)"></div>
  <div class="pg">08</div>
</section>

<!-- 9 -->
<section class="slide">
  <div class="ph" role="img" aria-label="Photo of a glass office corridor" style="left:0;top:0;width:210px;height:217px;background:linear-gradient(180deg,#d8dadb 0%,#a8acae 50%,#6d7072 100%)"></div>
  <div class="abs" style="left:18px;top:30px;width:150px;height:150px;background:rgba(155,135,90,.88)"></div>
  <div class="abs h wt" style="left:30px;top:45px;font-size:32px;font-weight:800">74%</div>
  <div class="abs tiny" style="left:30px;top:88px;width:120px;color:#fff">of buyers choose the same rep that was first to answer and engage.</div>
  <svg class="abs" style="left:230px;top:30px" width="18" height="160"><circle cx="9" cy="9" r="8" fill="#555"/><circle cx="9" cy="50" r="8" fill="#555"/><circle cx="9" cy="91" r="8" fill="#555"/><circle cx="9" cy="132" r="8" fill="#555"/></svg>
  <div class="abs tiny" style="left:256px;top:30px;width:115px">Lorem ipsum dolor sit amet, consectetur adipiscing elit sed do tempor.</div>
  <div class="abs tiny" style="left:256px;top:71px;width:115px">Lorem ipsum dolor sit amet, consectetur adipiscing elit sed do tempor.</div>
  <div class="abs tiny" style="left:256px;top:112px;width:115px">Lorem ipsum dolor sit amet, consectetur adipiscing elit sed do tempor.</div>
  <div class="abs tiny" style="left:256px;top:153px;width:115px">Lorem ipsum dolor sit amet, consectetur adipiscing elit sed do tempor.</div>
  <div class="pg">09</div>
</section>

<!-- 10 -->
<section class="slide">
  <div class="slide-title">Lorem ipsum dolor sit amet</div>
  <div class="brand-mini">KR TMW</div>
  <svg class="abs" style="left:40px;top:70px" width="140" height="60">
    <defs><g id="person"><circle cx="5" cy="3" r="3"/><rect x="1" y="7" width="8" height="12" rx="2"/></g></defs>
    <g fill="#555"><use href="#person" x="0"/><use href="#person" x="12"/><use href="#person" x="24"/><use href="#person" x="36"/><use href="#person" x="48"/><use href="#person" x="60"/></g>
    <g fill="#cfcfcf"><use href="#person" x="72"/><use href="#person" x="84"/><use href="#person" x="96"/><use href="#person" x="108"/></g>
    <g fill="#9b875a"><use href="#person" x="0" y="30"/><use href="#person" x="12" y="30"/><use href="#person" x="24" y="30"/></g>
    <g fill="#cfcfcf"><use href="#person" x="36" y="30"/><use href="#person" x="48" y="30"/><use href="#person" x="60" y="30"/><use href="#person" x="72" y="30"/><use href="#person" x="84" y="30"/><use href="#person" x="96" y="30"/><use href="#person" x="108" y="30"/></g>
  </svg>
  <div class="abs h" style="left:182px;top:76px;font-size:9px;color:var(--grey)">60 proc.</div>
  <div class="abs h" style="left:182px;top:106px;font-size:9px;color:var(--gold)">30 proc.</div>
  <div class="abs tiny" style="left:250px;top:74px;width:115px">Lorem ipsum dolor sit amet, consectetur adipiscing elit sed do eiusmod tempor.</div>
  <div class="abs tiny" style="left:250px;top:104px;width:115px">Lorem ipsum dolor sit amet, consectetur adipiscing elit sed do eiusmod tempor.</div>
  <div class="foot"></div><div class="pg">10</div>
</section>

<!-- 11 -->
<section class="slide">
  <div class="brand-mini">KR TMW</div>
  <div class="abs h" style="left:18px;top:42px;font-size:6px">Lorem ipsum dolor sit</div>
  <div class="abs tiny" style="left:18px;top:52px;width:100px">Ut enim ad minim veniam, quis nostrud exercitation ullamco laboris nisi ut aliquip ex ea commodo consequat. Duis aute irure dolor in reprehenderit in voluptate velit esse cillum dolore eu fugiat nulla pariatur. Excepteur sint occaecat cupidatat non proident, sunt in culpa qui officia deserunt mollit anim id est laborum sed ut perspiciatis.</div>
  <div class="ph" role="img" aria-label="Photo of a glass tower against a blue sky" style="left:132px;top:0;width:90px;height:190px;background:linear-gradient(180deg,#4f8fae 0%,#8fb7c6 40%,#d98a4a 75%,#5a4a3c 100%)"></div>
  <svg class="abs" style="left:290px;top:28px" width="14" height="120"><rect x="2" y="2" width="10" height="8" fill="none" stroke="#9b875a"/><path d="M2 48h10l-2 6H4z" fill="none" stroke="#9b875a"/><circle cx="6" cy="98" r="4" fill="none" stroke="#9b875a"/><line x1="9" y1="101" x2="13" y2="105" stroke="#9b875a"/></svg>
  <div class="abs tiny" style="left:240px;top:44px;width:125px"><b>Lorem ipsum dolor sit</b><br>Lorem ipsum dolor sit amet, consectetur adipiscing elit sed do.</div>
  <div class="abs tiny" style="left:240px;top:92px;width:125px"><b>Lorem ipsum dolor sit</b><br>Lorem ipsum dolor sit amet, consectetur adipiscing elit sed do.</div>
  <div class="abs tiny" style="left:240px;top:140px;width:125px"><b>Lorem ipsum dolor sit</b><br>Lorem ipsum dolor sit amet, consectetur adipiscing elit sed do.</div>
  <div class="foot"></div><div class="pg">11</div>
</section>

<!-- 12 -->
<section class="slide">
  <div class="slide-title">About Us</div>
  <div class="abs tiny" style="left:16px;top:72px;width:150px">Sed ut perspiciatis unde omnis iste natus error sit voluptatem accusantium doloremque laudantium, totam rem aperiam, eaque ipsa quae ab illo inventore veritatis et quasi architecto beatae vitae dicta sunt explicabo. <b>Nemo enim ipsam voluptatem</b> quia voluptas sit aspernatur aut odit aut fugit, sed quia consequuntur magni dolores eos qui ratione <b>voluptatem sequi nesciunt</b>.</div>
  <div class="abs" style="left:175px;top:0;width:211px;height:217px;background:var(--gold)"></div>
  <svg class="abs" style="left:185px;top:26px" width="14" height="160"><g fill="#fff"><path d="M2 2h10v5a5 5 0 0 1-10 0z"/><circle cx="6" cy="57" r="5" fill="none" stroke="#fff" stroke-width="1.5"/><circle cx="7" cy="103" r="5"/><rect x="1" y="143" width="12" height="10"/></g></svg>
  <div class="abs tiny" style="left:212px;top:22px;width:160px;color:#fff"><b style="color:#fff">Lorem ipsum dolor sit amet</b><br>Lorem ipsum dolor sit amet, consectetur adipiscing elit. Curabitur at felis tempor, blandit.</div>
  <div class="abs tiny" style="left:212px;top:68px;width:160px;color:#fff"><b style="color:#fff">Lorem ipsum dolor sit amet</b><br>Lorem ipsum dolor sit amet, consectetur adipiscing elit. Curabitur at felis tempor, blandit.</div>
  <div class="abs tiny" style="left:212px;top:114px;width:160px;color:#fff"><b style="color:#fff">Lorem ipsum dolor sit amet</b><br>Lorem ipsum dolor sit amet, consectetur adipiscing elit. Curabitur at felis tempor, blandit.</div>
  <div class="abs tiny" style="left:212px;top:160px;width:160px;color:#fff"><b style="color:#fff">Lorem ipsum dolor sit amet</b><br>Lorem ipsum dolor sit amet, consectetur adipiscing elit. Curabitur at felis tempor, blandit.</div>
  <div class="pg" style="color:#fff">12</div>
</section>

<!-- 13 -->
<section class="slide">
  <div class="slide-title">Lorem ipsum dolor sit amet</div>
  <svg class="abs" style="left:12px;top:58px" width="362" height="100">
    <polygon points="0,0 80,0 95,50 80,100 0,100 15,50" fill="#6f6440"/>
    <polygon points="88,0 168,0 183,50 168,100 88,100 103,50" fill="#c9a12a"/>
    <polygon points="176,0 256,0 271,50 256,100 176,100 191,50" fill="#c5601c"/>
    <polygon points="264,0 344,0 359,50 344,100 264,100 279,50" fill="#b9a67e"/>
    <g fill="none" stroke="#fff" stroke-width="1.5"><path d="M38 14l6 8 10-12"/><rect x="124" y="12" width="12" height="14"/><circle cx="219" cy="19" r="7"/><circle cx="304" cy="16" r="4"/><path d="M297 28a7 6 0 0 1 14 0"/></g>
    <g fill="#fff" font-family="Open Sans, sans-serif" font-size="5.5"><text x="22" y="48" font-weight="700">Lorem ipsum dolor</text><text x="110" y="48" font-weight="700">Lorem ipsum dolor</text><text x="198" y="48" font-weight="700">Lorem ipsum dolor</text><text x="286" y="48" font-weight="700">Lorem ipsum dolor</text>
    <text x="22" y="58">Lorem ipsum dolor sit</text><text x="22" y="66">amet adipiscing elit</text><text x="22" y="74">sed do eiusmod.</text>
    <text x="110" y="58">Lorem ipsum dolor sit</text><text x="110" y="66">amet adipiscing elit</text><text x="110" y="74">sed do eiusmod.</text>
    <text x="198" y="58">Lorem ipsum dolor sit</text><text x="198" y="66">amet adipiscing elit</text><text x="198" y="74">sed do eiusmod.</text>
    <text x="286" y="58">Lorem ipsum dolor sit</text><text x="286" y="66">amet adipiscing elit</text><text x="286" y="74">sed do eiusmod.</text></g>
  </svg>
  <div class="foot"></div><div class="pg">13</div>
</section>

<!-- 14 -->
<section class="slide">
  <div class="slide-title" style="font-size:13px">Our Services</div>
  <div class="abs tiny" style="left:16px;top:52px;width:75px"><b>Lorem ipsum dolor</b><br>Lorem ipsum dolor sit amet, consectetur adipiscing elit, sed do eiusmod tempor.</div>
  <div class="abs tiny" style="left:106px;top:52px;width:75px"><b>Lorem ipsum dolor</b><br>Lorem ipsum dolor sit amet, consectetur adipiscing elit, sed do eiusmod tempor.</div>
  <div class="abs tiny" style="left:196px;top:52px;width:75px"><b>Lorem ipsum dolor</b><br>Lorem ipsum dolor sit amet, consectetur adipiscing elit, sed do eiusmod tempor.</div>
  <div class="abs tiny" style="left:16px;top:118px;width:75px"><b>Lorem ipsum dolor</b><br>Lorem ipsum dolor sit amet, consectetur adipiscing elit, sed do eiusmod tempor.</div>
  <div class="abs tiny" style="left:106px;top:118px;width:75px"><b>Lorem ipsum dolor</b><br>Lorem ipsum dolor sit amet, consectetur adipiscing elit, sed do eiusmod tempor.</div>
  <div class="ph" role="img" aria-label="Photo of skyscrapers with sunlight between them" style="left:225px;top:0;width:161px;height:217px;clip-path:polygon(100% 0,100% 100%,0 100%);background:linear-gradient(200deg,#dce3e8 0%,#8c98a2 40%,#e9b866 70%,#3a3630 100%)"></div>
  <div class="pg">14</div>
</section>

<!-- 15 -->
<section class="slide">
  <div class="slide-title">Lorem ipsum dolor sit amet</div>
  <div class="brand-mini">KR TMW</div>
  <div class="abs tiny" style="left:16px;top:40px;width:150px">Lorem ipsum dolor sit amet, consectetur adipiscing elit, sed do eiusmod tempor incididunt ut labore et dolore magna aliqua enim.</div>
  <div class="ph" role="img" aria-label="Photo of a desk with a plant, notebook and glasses" style="left:16px;top:78px;width:150px;height:95px;background:linear-gradient(135deg,#e8ecea 0%,#b8c9b2 40%,#f2f2f2 70%,#9ea39e 100%)"></div>
  <svg class="abs" style="left:188px;top:40px" width="14" height="130"><g fill="#555"><circle cx="7" cy="7" r="6"/><circle cx="7" cy="35" r="6"/><circle cx="7" cy="63" r="6"/><circle cx="7" cy="91" r="6"/><circle cx="7" cy="119" r="6"/></g><g fill="#fff" font-size="5" font-family="Open Sans" text-anchor="middle"><text x="7" y="9">01</text><text x="7" y="37">02</text><text x="7" y="65">03</text><text x="7" y="93">04</text><text x="7" y="121">05</text></g></svg>
  <div class="abs tiny" style="left:208px;top:40px;width:160px"><b style="color:var(--gold)">Content Title #01</b><br>Write your text here for the summary.</div>
  <div class="abs tiny" style="left:208px;top:68px;width:160px"><b style="color:var(--gold)">Content Title #02</b><br>Write your text here for the summary.</div>
  <div class="abs tiny" style="left:208px;top:96px;width:160px"><b style="color:var(--gold)">Content Title #03</b><br>Write your text here for the summary.</div>
  <div class="abs tiny" style="left:208px;top:124px;width:160px"><b style="color:var(--gold)">Content Title #04</b><br>Write your text here for the summary.</div>
  <div class="abs tiny" style="left:208px;top:152px;width:160px"><b style="color:var(--gold)">Content Title #05</b><br>Write your text here for the summary.</div>
  <div class="foot"></div><div class="pg">15</div>
</section>

<!-- 16 -->
<section class="slide">
  <div class="slide-title">Lorem ipsum dolor sit amet</div>
  <div class="brand-mini">KR TMW</div>
  <div class="abs tiny" style="left:16px;top:42px;width:55px">Lorem ipsum dolor sit amet, consectetur adipiscing elit sed do eiusmod.</div>
  <div class="abs tiny" style="left:16px;top:100px;width:55px">Lorem ipsum dolor sit amet, consectetur adipiscing elit sed do eiusmod.</div>
  <svg class="abs" style="left:90px;top:44px" width="180" height="100">
    <g stroke="#e4e4e4" stroke-width=".6"><line x1="0" y1="10" x2="180" y2="10"/><line x1="0" y1="30" x2="180" y2="30"/><line x1="0" y1="50" x2="180" y2="50"/><line x1="0" y1="70" x2="180" y2="70"/><line x1="0" y1="90" x2="180" y2="90"/></g>
    <polyline points="10,80 40,60 60,70 90,45 120,55 150,30 175,12" fill="none" stroke="#c9b88f" stroke-width="1.4"/>
    <polyline points="10,88 40,78 60,82 90,70 120,72 150,60 175,52" fill="none" stroke="#9b875a" stroke-width="1"/>
  </svg>
  <div class="abs h" style="left:282px;top:64px;font-size:8px;color:var(--gold)">50%</div>
  <div class="abs h" style="left:282px;top:124px;font-size:8px;color:var(--gold)">18%</div>
  <div class="abs tiny" style="left:265px;top:56px;width:30px">Text here</div>
  <svg class="abs" style="left:318px;top:52px" width="40" height="130" fill="none" stroke="#9b875a" stroke-width="1.3"><polygon points="20,2 38,24 28,24 28,56 12,56 12,24 2,24"/><polygon points="20,126 38,104 28,104 28,72 12,72 12,104 2,104"/></svg>
  <div class="foot"></div><div class="pg">16</div>
</section>

<!-- 17 -->
<section class="slide">
  <div class="ph" role="img" aria-label="Blurred photo of an office interior with warm light" style="left:0;top:0;width:386px;height:100px;background:linear-gradient(100deg,#6e6a62 0%,#c2a24b 35%,#8f8a80 60%,#d4b460 100%)"></div>
  <div class="brand-mini" style="color:#fff">KR TMW</div>
  <div class="abs h wt" style="left:0;top:28px;width:386px;text-align:center;font-size:13px">Lorem ipsum dolor</div>
  <div class="abs" style="left:0;top:84px;width:386px;height:16px;background:rgba(122,106,67,.9)"></div>
  <svg class="abs" style="left:0;top:80px" width="386" height="26"><g fill="#7a6a43" stroke="#fff" stroke-width="1.5"><circle cx="83" cy="12" r="10"/><circle cx="193" cy="12" r="10"/><circle cx="303" cy="12" r="10"/></g><g fill="none" stroke="#fff" stroke-width="1.6"><path d="M78 12l4 4 6-7"/><path d="M188 12l4 4 6-7"/><path d="M298 12l4 4 6-7"/></g></svg>
  <div class="abs tiny" style="left:43px;top:116px;width:80px;text-align:center"><b>Lorem ipsum dolor</b><br>Lorem ipsum dolor sit amet, consectetur adipiscing elit, sed do eiusmod tempor.</div>
  <div class="abs tiny" style="left:153px;top:116px;width:80px;text-align:center"><b>Lorem ipsum dolor</b><br>Lorem ipsum dolor sit amet, consectetur adipiscing elit, sed do eiusmod tempor.</div>
  <div class="abs tiny" style="left:263px;top:116px;width:80px;text-align:center"><b>Lorem ipsum dolor</b><br>Lorem ipsum dolor sit amet, consectetur adipiscing elit, sed do eiusmod tempor.</div>
  <div class="foot"></div><div class="pg">17</div>
</section>

<!-- 18 -->
<section class="slide">
  <div class="ph" role="img" aria-label="Faded photo of city towers" style="inset:0;background:linear-gradient(180deg,#ffffff 0%,#f2f2f2 50%,#d9dadb 100%)"></div>
  <div class="slide-title" style="top:10px">Company Mission, Vision and Values</div>
  <svg class="abs" style="left:16px;top:38px" width="354" height="140">
    <g fill="#fff" stroke="#9b875a"><rect x="0" y="30" width="100" height="80"/><rect x="127" y="30" width="100" height="80"/><rect x="254" y="30" width="100" height="80"/></g>
    <circle cx="50" cy="20" r="14" fill="#6f6440"/><circle cx="177" cy="20" r="14" fill="#c5601c"/><circle cx="304" cy="20" r="14" fill="#c9a12a"/>
    <g fill="none" stroke="#fff" stroke-width="1.3"><circle cx="50" cy="20" r="6"/><circle cx="50" cy="20" r="2"/><ellipse cx="177" cy="20" rx="7" ry="4"/><circle cx="304" cy="18" r="5"/></g>
    <g fill="#c5601c"><circle cx="113" cy="70" r="7"/><circle cx="240" cy="70" r="7"/></g>
    <g fill="#fff"><polygon points="111,66 117,70 111,74"/><polygon points="238,66 244,70 238,74"/></g>
    <g font-family="Open Sans" font-size="5.5" font-weight="700" text-anchor="middle"><text x="50" y="44">Your Text Here</text><text x="177" y="44">Your Text Here</text><text x="304" y="44">Your Text Here</text></g>
    <g font-family="Open Sans" font-size="5" fill="#7c7c7c"><text x="8" y="56">Lorem ipsum dolor sit amet,</text><text x="8" y="64">consectetur adipiscing elit,</text><text x="8" y="72">sed do eiusmod tempor</text><text x="8" y="80">incididunt ut labore magna.</text>
    <text x="135" y="56">Lorem ipsum dolor sit amet,</text><text x="135" y="64">consectetur adipiscing elit,</text><text x="135" y="72">sed do eiusmod tempor</text><text x="135" y="80">incididunt ut labore magna.</text>
    <text x="262" y="56">Lorem ipsum dolor sit amet,</text><text x="262" y="64">consectetur adipiscing elit,</text><text x="262" y="72">sed do eiusmod tempor</text><text x="262" y="80">incididunt ut labore magna.</text></g>
  </svg>
  <div class="pg">18</div>
</section>

<!-- 19 -->
<section class="slide">
  <div class="ph" role="img" aria-label="Photo of hands holding a notepad with written notes" style="inset:0;background:linear-gradient(120deg,#c65a1c 0%,#8a5a3a 30%,#e8e6e0 55%,#6a6560 100%)"></div>
  <div class="abs" style="left:188px;top:14px;width:186px;height:178px;background:#fff"></div>
  <div class="abs h" style="left:198px;top:22px;font-size:8px;color:var(--gold)">Lorem ipsum dolor sit amet</div>
  <div class="abs tiny" style="left:198px;top:36px;width:166px">Ut enim ad minim veniam, quis nostrud exercitation ullamco laboris nisi ut aliquip ex ea commodo consequat. Duis aute irure dolor in reprehenderit in voluptate velit esse cillum dolore eu fugiat nulla pariatur sint.</div>
  <svg class="abs" style="left:200px;top:128px" width="160" height="16" fill="none" stroke="#555" stroke-width="1.2"><rect x="1" y="2" width="11" height="12"/><path d="M4 6h5M4 9h5"/><rect x="104" y="1" width="8" height="14" rx="1"/></svg>
  <div class="abs tiny" style="left:218px;top:128px;width:70px">Lorem ipsum dolor sit amet, consectetur adipiscing.</div>
  <div class="abs tiny" style="left:318px;top:128px;width:52px">Lorem ipsum dolor sit amet.</div>
  <div class="abs" style="left:0;top:178px;width:150px;height:16px;background:rgba(155,135,90,.95)"></div>
  <div class="abs h wt" style="left:8px;top:182px;font-size:7px">Lorem ipsum dolor sit amet</div>
  <div class="pg">19</div>
</section>

<!-- 20 -->
<section class="slide">
  <div class="slide-title">Lorem ipsum dolor</div>
  <div class="brand-mini">KR TMW</div>
  <div class="abs tiny" style="left:16px;top:42px;width:170px">Lorem ipsum dolor sit amet, consectetur adipiscing elit, sed do eiusmod tempor incididunt ut labore et dolore magna aliqua.<br><br>Ut enim ad minim veniam, quis nostrud exercitation ullamco laboris nisi ut aliquip ex ea commodo consequat. Duis aute irure dolor in reprehenderit in voluptate velit esse cillum dolore.</div>
  <svg class="abs" style="left:204px;top:38px" width="16" height="150"><g fill="#7a6a43"><circle cx="8" cy="8" r="7"/><circle cx="8" cy="38" r="7"/><circle cx="8" cy="68" r="7"/><circle cx="8" cy="98" r="7" fill="#9b875a"/><circle cx="8" cy="128" r="7" fill="#c9b88f"/></g><g fill="none" stroke="#fff" stroke-width="1.4"><path d="M5 8l2 2 4-4"/><path d="M5 38l2 2 4-4"/><path d="M5 68l2 2 4-4"/><path d="M5 98l2 2 4-4"/><path d="M5 128l2 2 4-4"/></g></svg>
  <div class="abs tiny" style="left:226px;top:38px;width:145px"><b style="color:var(--gold)">Lorem ipsum dolor</b><br>Lorem ipsum dolor sit amet, consectetur.</div>
  <div class="abs tiny" style="left:226px;top:68px;width:145px"><b style="color:var(--gold)">Lorem ipsum dolor</b><br>Lorem ipsum dolor sit amet, consectetur.</div>
  <div class="abs tiny" style="left:226px;top:98px;width:145px"><b style="color:var(--gold)">Lorem ipsum dolor</b><br>Lorem ipsum dolor sit amet, consectetur.</div>
  <div class="abs tiny" style="left:226px;top:128px;width:145px"><b style="color:var(--gold)">Lorem ipsum dolor</b><br>Lorem ipsum dolor sit amet, consectetur.</div>
  <div class="abs tiny" style="left:226px;top:158px;width:145px"><b style="color:var(--gold)">Lorem ipsum dolor</b><br>Lorem ipsum dolor sit amet, consectetur.</div>
  <div class="foot"></div><div class="pg">20</div>
</section>

<!-- 21 -->
<section class="slide">
  <div class="slide-title">Lorem ipsum dolor sit amet</div>
  <div class="brand-mini">KR TMW</div>
  <div class="abs tiny" style="left:16px;top:38px;width:110px">Lorem ipsum dolor sit amet, consectetur adipiscing elit, sed do eiusmod tempor incididunt ut labore et dolore magna aliqua. Ut enim ad minim veniam, quis nostrud exercitation ullamco laboris nisi ut aliquip ex ea commodo consequat duis aute irure.<br><br>Lorem ipsum dolor sit amet, consectetur adipiscing elit sed do eiusmod.</div>
  <div class="abs tiny" style="left:140px;top:38px;width:110px">Lorem ipsum dolor sit amet, consectetur adipiscing elit, sed do eiusmod tempor incididunt ut labore et dolore magna.</div>
  <div class="abs" style="left:140px;top:92px;width:110px;height:85px;background:var(--gold)"></div>
  <div class="abs tiny" style="left:148px;top:100px;width:95px;color:#fff"><b style="color:#fff">Lorem ipsum dolor</b><br>Lorem ipsum dolor sit amet, consectetur adipiscing elit, sed do eiusmod tempor incididunt ut labore et dolore.</div>
  <div class="abs tiny" style="left:264px;top:38px;width:110px">Lorem ipsum dolor sit amet, consectetur adipiscing elit, sed do eiusmod tempor.</div>
  <svg class="abs" style="left:264px;top:96px" width="8" height="80" fill="#7a6a43"><polygon points="0,0 7,4 0,8"/><polygon points="0,30 7,34 0,38"/><polygon points="0,60 7,64 0,68"/></svg>
  <div class="abs tiny" style="left:276px;top:94px;width:95px">Lorem ipsum dolor sit amet, consectetur adipiscing.</div>
  <div class="abs tiny" style="left:276px;top:124px;width:95px">Lorem ipsum dolor sit amet, consectetur adipiscing.</div>
  <div class="abs tiny" style="left:276px;top:154px;width:95px">Lorem ipsum dolor sit amet, consectetur adipiscing.</div>
  <div class="foot"></div><div class="pg">21</div>
</section>

<!-- 22 -->
<section class="slide">
  <div class="abs h" style="left:18px;top:56px;font-size:13px">Lorem ipsum dolor</div>
  <svg class="abs" style="left:120px;top:20px" width="120" height="170" viewBox="0 0 120 170">
    <g fill="none" stroke-width="24" transform="rotate(-90 60 85)">
      <circle cx="60" cy="85" r="40" stroke="#c9a12a" stroke-dasharray="38.9 212.4" stroke-dashoffset="0"/>
      <circle cx="60" cy="85" r="40" stroke="#bdbdbd" stroke-dasharray="38.9 212.4" stroke-dashoffset="-41.9"/>
      <circle cx="60" cy="85" r="40" stroke="#9b875a" stroke-dasharray="38.9 212.4" stroke-dashoffset="-83.8"/>
      <circle cx="60" cy="85" r="40" stroke="#c5601c" stroke-dasharray="38.9 212.4" stroke-dashoffset="-125.7"/>
      <circle cx="60" cy="85" r="40" stroke="#bdbdbd" stroke-dasharray="38.9 212.4" stroke-dashoffset="-167.6"/>
      <circle cx="60" cy="85" r="40" stroke="#7a6a43" stroke-dasharray="38.9 212.4" stroke-dashoffset="-209.5"/>
    </g>
  </svg>
  <div class="abs h" style="left:248px;top:20px;font-size:8px;color:var(--grey)">01</div>
  <div class="abs h" style="left:262px;top:62px;font-size:8px;color:var(--grey)">02</div>
  <div class="abs h" style="left:262px;top:128px;font-size:8px;color:var(--grey)">03</div>
  <div class="abs h" style="left:248px;top:170px;font-size:8px;color:var(--grey)">04</div>
  <div class="abs h" style="left:96px;top:170px;font-size:8px;color:var(--grey)">05</div>
  <div class="abs h" style="left:36px;top:120px;font-size:8px;color:var(--grey)">06</div>
  <div class="abs tiny" style="left:262px;top:20px;width:100px">Lorem ipsum dolor sit amet, consectetur adipiscing.</div>
  <div class="abs tiny" style="left:276px;top:62px;width:100px">Lorem ipsum dolor sit amet, consectetur adipiscing.</div>
  <div class="abs tiny" style="left:276px;top:128px;width:100px">Lorem ipsum dolor sit amet, consectetur adipiscing.</div>
  <div class="abs tiny" style="left:262px;top:170px;width:100px">Lorem ipsum dolor sit amet, consectetur adipiscing.</div>
  <div class="abs tiny" style="left:110px;top:170px;width:70px">Lorem ipsum dolor sit amet.</div>
  <div class="abs tiny" style="left:50px;top:120px;width:70px">Lorem ipsum dolor sit amet, consectetur.</div>
  <div class="pg">22</div>
</section>

<!-- 23 -->
<section class="slide">
  <div class="ph" role="img" aria-label="Photo looking up at glass skyscrapers against a cloudy sky" style="inset:0;background:linear-gradient(160deg,#3f6a8f 0%,#a9c3d9 35%,#e8eef3 50%,#6f8aa4 75%,#2f3f52 100%)"></div>
  <div class="abs h wt" style="left:18px;top:12px;font-size:10px">Lorem ipsum dolor sit amet</div>
  <div class="abs" style="left:18px;top:128px;width:340px;height:18px;background:rgba(110,110,110,.85)"></div>
  <div class="abs" style="left:18px;top:150px;width:340px;height:18px;background:rgba(197,96,28,.9)"></div>
  <div class="abs" style="left:18px;top:172px;width:340px;height:18px;background:rgba(201,161,42,.9)"></div>
  <div class="abs tiny" style="left:26px;top:133px;color:#fff">Lorem ipsum dolor sit amet</div>
  <div class="abs tiny" style="left:26px;top:155px;color:#fff">Lorem ipsum dolor sit amet</div>
  <div class="abs tiny" style="left:26px;top:177px;color:#fff">Lorem ipsum dolor sit amet</div>
  <div class="abs h wt" style="left:300px;top:131px;font-size:10px">$ 64,090</div>
  <div class="abs h wt" style="left:300px;top:153px;font-size:10px">$124,090</div>
  <div class="abs h wt" style="left:300px;top:175px;font-size:10px">$234,090</div>
  <div class="pg" style="color:#fff">23</div>
</section>

<!-- 24 -->
<section class="slide" style="background:linear-gradient(180deg,#9b875a 0%,#c9b88f 100%)">
  <div class="slide-title wt">Pricing Tables</div>
  <div class="brand-mini" style="color:#fff">KR TMW</div>
  <div class="abs" style="left:60px;top:80px;width:84px;height:95px;background:#fff"></div>
  <div class="abs" style="left:150px;top:66px;width:86px;height:115px;background:#fff;box-shadow:0 2px 6px rgba(0,0,0,.15)"></div>
  <div class="abs" style="left:242px;top:80px;width:84px;height:95px;background:#fff"></div>
  <svg class="abs" style="left:60px;top:52px" width="266" height="64"><g fill="#7a6a43" stroke="#fff" stroke-width="2"><circle cx="42" cy="40" r="16"/><circle cx="133" cy="28" r="18"/><circle cx="224" cy="40" r="16"/></g><g fill="#fff" font-family="Montserrat" font-weight="700" text-anchor="middle" font-size="9"><text x="42" y="43">$25</text><text x="133" y="31">$50</text><text x="224" y="43">$99</text></g></svg>
  <div class="abs tiny" style="left:66px;top:118px;width:72px;text-align:center">Lorem ipsum dolor sit amet, consectetur adipiscing elit.</div>
  <div class="abs tiny" style="left:156px;top:110px;width:74px;text-align:center">Lorem ipsum dolor sit amet, consectetur adipiscing elit.</div>
  <div class="abs tiny" style="left:248px;top:118px;width:72px;text-align:center">Lorem ipsum dolor sit amet, consectetur adipiscing elit.</div>
  <div class="abs tiny" style="left:74px;top:158px;width:56px;height:11px;line-height:11px;border-radius:6px;text-align:center;background:var(--gold);color:#fff">Lorem ipsum</div>
  <div class="abs tiny" style="left:165px;top:166px;width:56px;height:11px;line-height:11px;border-radius:6px;text-align:center;background:var(--gold);color:#fff">Lorem ipsum</div>
  <div class="abs tiny" style="left:256px;top:158px;width:56px;height:11px;line-height:11px;border-radius:6px;text-align:center;background:var(--gold);color:#fff">Lorem ipsum</div>
  <div class="pg" style="color:#fff">24</div>
</section>

<!-- 25 -->
<section class="slide">
  <div class="slide-title">Pricing Tables</div>
  <div class="brand-mini">KR TMW</div>
  <div class="abs" style="left:16px;top:58px;width:354px;height:110px;display:flex;gap:10px">
    <div style="position:relative;flex:1;box-shadow:0 1px 4px rgba(0,0,0,.2);background:#fff"><div class="h" style="font-size:6px;margin:6px 0 0 8px">Lorem ipsum dolor</div><div class="h" style="font-size:15px;margin-left:8px">$10<span style="font-size:6px">/yr</span></div><div class="tiny" style="margin:4px 8px">Lorem ipsum dolor<br>Lorem ipsum dolor<br>Lorem ipsum dolor<br>Lorem ipsum dolor</div><div class="tiny" style="position:absolute;left:0;right:0;bottom:0;height:12px;line-height:12px;background:var(--gold);color:#fff;text-align:center">Lorem ipsum dolor</div></div>
    <div style="position:relative;flex:1;box-shadow:0 1px 4px rgba(0,0,0,.2);background:#fff"><div class="h" style="font-size:6px;margin:6px 0 0 8px">Lorem ipsum dolor</div><div class="h" style="font-size:15px;margin-left:8px">$99<span style="font-size:6px">/yr</span></div><div class="tiny" style="margin:4px 8px">Lorem ipsum dolor<br>Lorem ipsum dolor<br>Lorem ipsum dolor<br>Lorem ipsum dolor</div><div class="tiny" style="position:absolute;left:0;right:0;bottom:0;height:12px;line-height:12px;background:var(--gold);color:#fff;text-align:center">Lorem ipsum dolor</div></div>
    <div style="position:relative;flex:1;box-shadow:0 1px 4px rgba(0,0,0,.2);background:#fff"><div class="h" style="font-size:6px;margin:6px 0 0 8px">Lorem ipsum dolor</div><div class="h" style="font-size:15px;margin-left:8px">$100<span style="font-size:6px">/yr</span></div><div class="tiny" style="margin:4px 8px">Lorem ipsum dolor<br>Lorem ipsum dolor<br>Lorem ipsum dolor<br>Lorem ipsum dolor</div><div class="tiny" style="position:absolute;left:0;right:0;bottom:0;height:12px;line-height:12px;background:var(--gold);color:#fff;text-align:center">Lorem ipsum dolor</div></div>
    <div style="position:relative;flex:1;box-shadow:0 1px 4px rgba(0,0,0,.2);background:#fff"><div class="h" style="font-size:6px;margin:6px 0 0 8px">Lorem ipsum dolor</div><div class="h" style="font-size:15px;margin-left:8px">$199<span style="font-size:6px">/yr</span></div><div class="tiny" style="margin:4px 8px">Lorem ipsum dolor<br>Lorem ipsum dolor<br>Lorem ipsum dolor<br>Lorem ipsum dolor</div><div class="tiny" style="position:absolute;left:0;right:0;bottom:0;height:12px;line-height:12px;background:var(--gold);color:#fff;text-align:center">Lorem ipsum dolor</div></div>
  </div>
  <div class="foot"></div><div class="pg">25</div>
</section>

<!-- 26 -->
<section class="slide">
  <div class="slide-title">Lorem ipsum dolor</div>
  <div class="brand-mini">KR TMW</div>
  <svg class="abs" style="left:16px;top:38px" width="354" height="150" font-family="Open Sans" font-size="5.5">
    <rect x="110" y="0" width="48" height="16" fill="#c5601c"/><rect x="158" y="0" width="48" height="16" fill="#9b875a"/><rect x="206" y="0" width="48" height="16" fill="#6f6440"/><rect x="254" y="0" width="48" height="16" fill="#4c9a3a"/><rect x="302" y="0" width="52" height="16" fill="#3b7bbf"/>
    <g fill="#fff" text-anchor="middle"><text x="134" y="10">Lorem ipsum</text><text x="182" y="10">Lorem ipsum</text><text x="230" y="10">Lorem ipsum</text><text x="278" y="10">Lorem ipsum</text><text x="328" y="10">Lorem ipsum</text></g>
    <g fill="#ececec"><rect x="0" y="18" width="354" height="16"/><rect x="0" y="54" width="354" height="16"/><rect x="0" y="90" width="354" height="16"/><rect x="0" y="126" width="354" height="16"/></g>
    <g fill="#f7f7f7"><rect x="0" y="36" width="354" height="16"/><rect x="0" y="72" width="354" height="16"/><rect x="0" y="108" width="354" height="16"/></g>
    <g fill="#262626"><text x="6" y="29">Lorem ipsum dolor sit amet</text><text x="6" y="47">Lorem ipsum dolor sit amet</text><text x="6" y="65">Lorem ipsum dolor sit amet</text><text x="6" y="83">Lorem ipsum dolor sit amet</text><text x="6" y="101">Lorem ipsum dolor sit amet</text><text x="6" y="119">Lorem ipsum dolor sit amet</text><text x="6" y="137">Lorem ipsum dolor sit amet</text></g>
    <g fill="#262626" text-anchor="middle">
      <text x="134" y="29">23</text><text x="182" y="29">45</text><text x="230" y="29">4</text><text x="278" y="29">4</text><text x="328" y="29">34</text>
      <text x="134" y="47">234</text><text x="182" y="47">75</text><text x="230" y="47">4</text><text x="278" y="47">4</text><text x="328" y="47">66</text>
      <text x="134" y="65">23</text><text x="182" y="65">75</text><text x="230" y="65">64</text><text x="278" y="65">6</text><text x="328" y="65">44</text>
      <text x="134" y="83">95</text><text x="182" y="83">45</text><text x="230" y="83">4</text><text x="278" y="83">4</text><text x="328" y="83">34</text>
      <text x="134" y="101">23</text><text x="182" y="101">45</text><text x="230" y="101">44</text><text x="278" y="101">4</text><text x="328" y="101">34</text>
      <text x="134" y="119">76</text><text x="182" y="119">64</text><text x="230" y="119">46</text><text x="278" y="119">4</text><text x="328" y="119">56</text>
      <text x="134" y="137">23</text><text x="182" y="137">45</text><text x="230" y="137">44</text><text x="278" y="137">6</text><text x="328" y="137">34</text>
    </g>
  </svg>
  <div class="foot"></div><div class="pg">26</div>
</section>

<!-- 27 -->
<section class="slide" style="background:linear-gradient(180deg,#a5916a 0%,#c2b08a 100%)">
  <div class="slide-title wt" style="font-size:10px">Sed ut perspiciatis, unde omnis iste natus</div>
  <div class="brand-mini" style="color:#fff">KR TMW</div>
  <svg class="abs" style="left:16px;top:34px" width="354" height="110" font-family="Open Sans" font-size="4.5" fill="#fff">
    <g stroke="rgba(255,255,255,.35)" stroke-width=".6"><line x1="20" y1="10" x2="354" y2="10"/><line x1="20" y1="30" x2="354" y2="30"/><line x1="20" y1="50" x2="354" y2="50"/><line x1="20" y1="70" x2="354" y2="70"/><line x1="20" y1="90" x2="354" y2="90"/></g>
    <text x="0" y="12">2500</text><text x="0" y="32">2000</text><text x="0" y="52">1500</text><text x="0" y="72">1000</text><text x="0" y="92">500</text>
    <polyline points="30,70 85,55 140,72 195,60 250,65 305,40 350,30" fill="none" stroke="#fff" stroke-width="1"/>
    <polyline points="30,50 85,75 140,60 195,80 250,45 305,55 350,12" fill="none" stroke="#f2dd2a" stroke-width="1.3"/>
    <g fill="#fff"><circle cx="30" cy="70" r="1.6"/><circle cx="85" cy="55" r="1.6"/><circle cx="140" cy="72" r="1.6"/><circle cx="195" cy="60" r="1.6"/><circle cx="250" cy="65" r="1.6"/><circle cx="305" cy="40" r="1.6"/></g>
    <text x="22" y="104">Item 1</text><text x="77" y="104">Item 2</text><text x="132" y="104">Item 3</text><text x="187" y="104">Item 4</text><text x="242" y="104">Item 5</text><text x="297" y="104">Item 6</text>
  </svg>
  <div class="abs h wt" style="left:16px;top:160px;font-size:16px">57<span style="font-size:9px">%</span></div>
  <div class="abs tiny" style="left:52px;top:158px;width:120px;color:#fff"><b style="color:#fff">Contents Title</b><br>Lorem ipsum dolor sit amet, consectetur adipiscing elit sed do eiusmod tempor.</div>
  <div class="abs h wt" style="left:200px;top:160px;font-size:16px">79<span style="font-size:9px">%</span></div>
  <div class="abs tiny" style="left:236px;top:158px;width:120px;color:#fff"><b style="color:#fff">Contents Title</b><br>Lorem ipsum dolor sit amet, consectetur adipiscing elit sed do eiusmod tempor.</div>
  <div class="pg" style="color:#fff">27</div>
</section>

<!-- 28 -->
<section class="slide">
  <div class="slide-title">Timeline</div>
  <svg class="abs" style="left:10px;top:52px" width="366" height="120" font-family="Open Sans" font-size="5">
    <rect x="0" y="40" width="30" height="30" fill="#fff" stroke="#9b875a"/>
    <circle cx="15" cy="52" r="5" fill="none" stroke="#9b875a" stroke-width="1.3"/><rect x="12" y="58" width="6" height="4" fill="#9b875a"/>
    <rect x="50" y="52" width="75" height="8" fill="#555"/><rect x="125" y="52" width="75" height="8" fill="#9b875a"/><rect x="200" y="52" width="75" height="8" fill="#c5601c"/><rect x="275" y="52" width="75" height="8" fill="#9b875a"/>
    <g fill="#fff" text-anchor="middle" font-weight="700"><text x="87" y="58">2012</text><text x="162" y="58">2013</text><text x="237" y="58">2014</text><text x="312" y="58">2015</text></g>
    <g stroke="#9b875a" stroke-width=".6"><line x1="87" y1="52" x2="87" y2="18"/><line x1="237" y1="52" x2="237" y2="18"/><line x1="162" y1="60" x2="162" y2="94"/><line x1="312" y1="60" x2="312" y2="94"/></g>
    <g fill="#9b875a"><circle cx="87" cy="18" r="1.8"/><circle cx="237" cy="18" r="1.8"/><circle cx="162" cy="94" r="1.8"/><circle cx="312" cy="94" r="1.8"/></g>
    <g fill="#7c7c7c"><text x="92" y="10" fill="#262626" font-weight="700">Update Here</text><text x="92" y="17">Lorem ipsum dolor</text><text x="92" y="24">sit amet adipiscing</text>
    <text x="242" y="10" fill="#262626" font-weight="700">Update Here</text><text x="242" y="17">Lorem ipsum dolor</text><text x="242" y="24">sit amet adipiscing</text>
    <text x="167" y="92" fill="#262626" font-weight="700">Update Here</text><text x="167" y="99">Lorem ipsum dolor</text><text x="167" y="106">sit amet adipiscing</text>
    <text x="317" y="92" fill="#262626" font-weight="700">Update Here</text><text x="317" y="99">Lorem ipsum dolor</text><text x="317" y="106">sit amet adipiscing</text></g>
  </svg>
  <div class="foot"></div><div class="pg">28</div>
</section>

<!-- 29 -->
<section class="slide">
  <div class="slide-title">Timeline</div>
  <svg class="abs" style="left:10px;top:52px" width="366" height="120" font-family="Open Sans" font-size="5">
    <rect x="0" y="52" width="75" height="8" fill="#9b875a"/><rect x="75" y="52" width="75" height="8" fill="#555"/><rect x="150" y="52" width="75" height="8" fill="#9b875a"/><rect x="225" y="52" width="75" height="8" fill="#555"/>
    <g fill="#fff" text-anchor="middle" font-weight="700"><text x="37" y="58">2016</text><text x="112" y="58">2017</text><text x="187" y="58">2018</text><text x="262" y="58">2019</text></g>
    <rect x="322" y="40" width="30" height="30" fill="#fff" stroke="#9b875a"/>
    <path d="M330 62l8-12 8-4-4 8-12 8z" fill="#9b875a"/>
    <g stroke="#9b875a" stroke-width=".6"><line x1="37" y1="60" x2="37" y2="94"/><line x1="187" y1="60" x2="187" y2="94"/><line x1="112" y1="52" x2="112" y2="18"/><line x1="262" y1="52" x2="262" y2="18"/></g>
    <g fill="#9b875a"><circle cx="37" cy="94" r="1.8"/><circle cx="187" cy="94" r="1.8"/><circle cx="112" cy="18" r="1.8"/><circle cx="262" cy="18" r="1.8"/></g>
    <g fill="#7c7c7c"><text x="117" y="10" fill="#262626" font-weight="700">Update Here</text><text x="117" y="17">Lorem ipsum dolor</text><text x="117" y="24">sit amet adipiscing</text>
    <text x="267" y="10" fill="#262626" font-weight="700">Update Here</text><text x="267" y="17">Lorem ipsum dolor</text><text x="267" y="24">sit amet adipiscing</text>
    <text x="42" y="92" fill="#262626" font-weight="700">Update Here</text><text x="42" y="99">Lorem ipsum dolor</text><text x="42" y="106">sit amet adipiscing</text>
    <text x="192" y="92" fill="#262626" font-weight="700">Update Here</text><text x="192" y="99">Lorem ipsum dolor</text><text x="192" y="106">sit amet adipiscing</text></g>
  </svg>
  <div class="foot"></div><div class="pg">29</div>
</section>

<!-- 30 -->
<section class="slide">
  <div class="slide-title">Lorem ipsum dolor sit amet</div>
  <div class="brand-mini">KR TMW</div>
  <svg class="abs" style="left:50px;top:34px" width="290" height="170" font-family="Open Sans" font-size="5">
    <circle cx="12" cy="9" r="7" fill="none" stroke="#4c9a3a" stroke-width="1.3"/><path d="M8 9l3 3 5-6" fill="none" stroke="#4c9a3a" stroke-width="1.3"/>
    <circle cx="162" cy="9" r="7" fill="none" stroke="#c5601c" stroke-width="1.3"/><path d="M159 6l6 6M165 6l-6 6" stroke="#c5601c" stroke-width="1.3"/>
    <rect x="0" y="20" width="135" height="140" fill="#f3f3f3"/><rect x="150" y="20" width="135" height="140" fill="#f3f3f3"/>
    <rect x="0" y="20" width="135" height="12" fill="#4c9a3a"/><rect x="150" y="20" width="135" height="12" fill="#c5601c"/>
    <g fill="#fff" font-weight="700" text-anchor="middle"><text x="67" y="28">POSITIVE POINTS</text><text x="217" y="28">NEGATIVE POINTS</text></g>
    <g fill="none" stroke="#4c9a3a" stroke-width="1"><circle cx="12" cy="46" r="5"/><circle cx="12" cy="76" r="5"/><circle cx="12" cy="106" r="5"/><circle cx="12" cy="136" r="5"/><path d="M9.5 46l2 2 3-4M9.5 76l2 2 3-4M9.5 106l2 2 3-4M9.5 136l2 2 3-4"/></g>
    <g fill="none" stroke="#c5601c" stroke-width="1"><circle cx="162" cy="46" r="5"/><circle cx="162" cy="76" r="5"/><circle cx="162" cy="106" r="5"/><circle cx="162" cy="136" r="5"/><path d="M160 44l4 4M164 44l-4 4M160 74l4 4M164 74l-4 4M160 104l4 4M164 104l-4 4M160 134l4 4M164 134l-4 4"/></g>
    <g fill="#262626" font-weight="700"><text x="22" y="44">TITLE GOES HERE</text><text x="22" y="74">TITLE GOES HERE</text><text x="22" y="104">TITLE GOES HERE</text><text x="22" y="134">TITLE GOES HERE</text></g>
    <g fill="#c5601c" font-weight="700"><text x="172" y="44">TITLE GOES HERE</text><text x="172" y="74">TITLE GOES HERE</text><text x="172" y="104">TITLE GOES HERE</text><text x="172" y="134">TITLE GOES HERE</text></g>
    <g fill="#7c7c7c"><text x="22" y="51">Text a short point for the list.</text><text x="22" y="81">Text a short point for the list.</text><text x="22" y="111">Text a short point for the list.</text><text x="22" y="141">Text a short point for the list.</text>
    <text x="172" y="51">Text a short point for the list.</text><text x="172" y="81">Text a short point for the list.</text><text x="172" y="111">Text a short point for the list.</text><text x="172" y="141">Text a short point for the list.</text></g>
  </svg>
  <div class="pg">30</div>
</section>

<div class="deck-end">
<!-- 31 -->
<section class="slide">
  <div class="ph" role="img" aria-label="Photo of a businessman touching a digital screen" style="left:0;top:0;width:386px;height:180px;background:linear-gradient(100deg,#2f4a66 0%,#5c7893 40%,#a9b8c6 65%,#3c4f62 100%)"></div>
  <div class="abs h wt" style="left:22px;top:58px;font-size:13px">Get In Touch</div>
  <div class="abs tiny" style="left:22px;top:80px;width:110px;color:#fff">Lorem ipsum dolor sit amet, consectetur adipiscing elit, sed do eiusmod tempor incididunt ut labore et dolore magna aliqua.</div>
  <svg class="abs" style="left:160px;top:58px" width="110" height="30" fill="none" stroke="#fff" stroke-width="1.6"><rect x="4" y="4" width="14" height="22" rx="2"/><rect x="36" y="7" width="26" height="17"/><path d="M36 7l13 10 13-10"/><circle cx="92" cy="15" r="5"/><path d="M97 15v3a3 3 0 0 0 6 0v-3a11 11 0 1 0-4 8"/></svg>
  <svg class="abs" style="left:16px;top:188px" width="360" height="16" fill="#9b875a"><circle cx="6" cy="8" r="6"/><rect x="88" y="2" width="12" height="12" rx="6"/><rect x="180" y="3" width="12" height="9"/><path d="M280 2a5 5 0 0 1 5 5c0 4-5 8-5 8s-5-4-5-8a5 5 0 0 1 5-5z"/></svg>
  <div class="abs tiny" style="left:30px;top:192px;color:var(--ink)">555 014 2290</div>
  <div class="abs tiny" style="left:120px;top:192px;color:var(--ink)">www.krtmw-demo.com</div>
  <div class="abs tiny" style="left:212px;top:192px;color:var(--ink)">hello@krtmw-demo.com</div>
  <div class="abs tiny" style="left:304px;top:188px;width:70px;color:var(--ink)">Here is our place,<br>Company address</div>
</section>

<!-- 32 -->
<section class="slide" style="background:linear-gradient(135deg,#9b875a 0%,#b9a67e 55%,#8e7b51 100%)">
  <div class="brand-mini" style="top:12px;right:24px;color:#fff;font-size:8px">KR TMW</div>
  <div class="abs h wt" style="left:20px;top:110px;font-size:22px;line-height:1.05;font-weight:800">THANK YOU FOR<br><span style="color:var(--gold-pale)">WATCHING!</span></div>
  <div class="abs h wt" style="left:22px;top:168px;font-size:7px;font-weight:600">ANY QUESTIONS?</div>
  <div class="pg" style="color:#fff">32</div>
</section>
</div>

</main>
</body>
</html>
```